Unique Private Wine Label for Wine Bottles (UPDATED BRIEF)

Updated Brief Oct 15, 2017. Please see below!

I am looking for a unique wine label designs for my wine bottles. I create wine and would like to have wine labels for my bottles. I am looking for a main label and then several additional labels with the same design just with the type of wine listed on the label (see below for wine types). This is private wine for family and friends to consume not commercially produced wine.

I would like a rustic, classic or vintage design with some color in the label. I do have a specific name for the wine which i like to call "Fernhollow" . I would like to see different designs.

We would like vintage or classic labels. Please give me a few multiple designs based on above. I also want to have a main label and then incorporate different types of wine into the labels like "Chardonnay" or "Pinot Noir" or "Sauvignon Blanc" or "Caberent Savignon" or "Merlot" below the name of the wine. As an example, the labels will be the same design but the word Sauvignon Blanc will be incorporated into the design for this type of wine label and so on for the other types of wine.

Please let me know if you have any questions.
Updates

Project Deadline Extended
Reason: I Have changed the vision of the design. I would like a classic, rustic or vintage design NOT a beach theme. The brief has been updated as of Oct 15, 2017. Please see updated brief for instructions on new design

Note: I have changed the vision of the design. I would like a classic, rustic or vintage design NOT a beach theme. The brief has been updated as of Oct 15, 2017. Please see updated brief for instructions on new design. I would like new designers to provide new designs! Payment is Guaranteed! Thanks!

Target Market(s)

This is private wine for family and friends to consume not commercially produced wine.

Font styles to use
Decorative
Script

Colors

Designer to choose colors to be used in the design.

Requirements
Must have
• Updated Brief Oct 15, 2017. Please see below!
• I am looking for a unique wine label designs for my wine bottles. I create wine and would like to have wine labels for my bottles. I am looking for a main label and then several additional labels with the same design just with the type of wine listed on the label (see below for wine types). This is private wine for family and friends to consume not commercially produced wine.
• I would like a rustic, classic or vintage design with some color in the label. I do have a specific name for the wine which i like to call "Fernhollow". I would like to see different designs.
• We would like vintage or classic labels. Please give me a few multiple designs based on above. I also want to have a main label and then incorporate different types of wine into the labels like "Chardonnay" or "Pinot Noir" or "Sauvignon Blanc" or "Caberent Savignon" or "Merlot" below the name of the wine. As an example, the labels will be the same design but the word Sauvignon Blanc will be incorporated into the design for this type of wine label and so on for the other types of wine.
• Please let me know if you have any questions.
Nice to have
Should not have
• Please see the updated brief instructions above. I DO NOT WANT A BEACH THEME ANYMORE!

```html
<!DOCTYPE html>
<html lang="en">
<head>
<meta charset="utf-8">
<title>Fernhollow Vineyards – Sauvignon Blanc Label</title>
<link href="https://fonts.googleapis.com/css2?family=Cinzel+Decorative:wght@400;700&family=Cinzel:wght@700&family=Pinyon+Script&display=swap" rel="stylesheet">
<style>
  :root {
    --page: #f4f4f4;
    --label-black: #0b0b0b;
    --gold: #d4b05a;
    --gold-light: #ead693;
    --cream: #f1e4b8;
    --ink: #141414;
  }
  html, body {
    margin: 0;
    padding: 0;
    width: 900px;
    height: 1200px;
    overflow: hidden;
    background: var(--page);
  }
  .canvas {
    position: relative;
    width: 900px;
    height: 1200px;
  }
  .wine-label {
    position: absolute;
    left: 144px;
    top: 100px;
    width: 612px;
    height: 1000px;
    background: var(--label-black);
  }
  .scene-panel {
    position: absolute;
    left: 111px;
    top: 114px;
    width: 388px;
    height: 388px;
  }
  .scene-panel svg { display: block; }
  .name-panel {
    position: absolute;
    left: 111px;
    top: 527px;
    width: 388px;
    height: 330px;
    box-sizing: border-box;
    border: 2px solid var(--gold-light);
    background: var(--gold);
    text-align: center;
  }
  .varietal {
    margin: 36px 0 0;
    font-family: "Cinzel Decorative", serif;
    font-weight: 400;
    font-size: 46px;
    line-height: 0.86;
    color: var(--ink);
    letter-spacing: -1px;
  }
  .vintage {
    margin: 22px 0 0;
    font-family: "Cinzel Decorative", serif;
    font-size: 66px;
    line-height: 1;
    color: var(--cream);
    text-shadow: 1px 1px 0 #5a4520, -1px -1px 0 #5a4520, 1px -1px 0 #5a4520, -1px 1px 0 #5a4520;
  }
  .estate-strip {
    position: absolute;
    left: 0;
    right: 0;
    bottom: 0;
    height: 78px;
    background: var(--label-black);
    display: flex;
    align-items: center;
    justify-content: center;
  }
  .estate-name {
    font-family: "Pinyon Script", cursive;
    font-size: 40px;
    color: var(--cream);
    white-space: nowrap;
  }
  .label-footer {
    position: absolute;
    left: 111px;
    width: 388px;
    top: 900px;
    display: flex;
    justify-content: space-between;
    font-family: "Cinzel", serif;
    font-weight: 700;
    font-size: 19px;
    color: var(--cream);
  }
</style>
</head>
<body>
<div class="canvas">
  <section class="wine-label">
    <div class="scene-panel">
      <svg width="388" height="388" viewBox="0 0 388 388" role="img" aria-label="Black and white photograph of a rocky shoreline with sand and clouded sky">
        <defs>
          <linearGradient id="shoreTone" x1="0" y1="0" x2="0" y2="1">
            <stop offset="0" stop-color="#9a9a9a"/>
            <stop offset="0.3" stop-color="#d6d6d6"/>
            <stop offset="0.5" stop-color="#3a3a3a"/>
            <stop offset="0.7" stop-color="#8c8c8c"/>
            <stop offset="1" stop-color="#b4b4b4"/>
          </linearGradient>
        </defs>
        <polygon class="gold-rule" points="0,0 388,204 388,216 0,12" fill="#d4b05a"/>
        <polygon class="shore-photo" points="0,26 388,222 388,388 0,388" fill="url(#shoreTone)"/>
      </svg>
    </div>

    <div class="name-panel">
      <h1 class="varietal">Sauvignon<br>Blanc</h1>
      <p class="vintage">2017</p>
      <div class="estate-strip">
        <span class="estate-name">Fernhollow Vineyards</span>
      </div>
    </div>

    <div class="label-footer">
      <span class="volume">75cl</span>
      <span class="abv">ALC.11%V/V</span>
    </div>
  </section>
</div>
</body>
</html>
```